Powerpoint template for Trivia Company

Revamp of our current powerpoint template to make it more professional and fun for the players. Something worthy of a trivia company. Please see logo attached for potential colour - but also open to other ideas.

NO BRANDING REQUIRED (IE: No mention of our company or logo on the template please)

Target Market(s)

Bars/restaurants

Colors
3176b5
00a990

```html
<!DOCTYPE html>
<html lang="en">
<head>
<meta charset="utf-8">
<title>Trivia Night – General Knowledge</title>
<link href="https://fonts.googleapis.com/css2?family=Montserrat:wght@500;600;700&display=swap" rel="stylesheet">
<style>
  :root {
    --page: #000000;
    --panel-deep: #0a141c;
    --panel-mid: #1d3a52;
    --band: rgba(40, 44, 48, 0.85);
    --teal: #00a990;
    --blue: #3176b5;
    --text: #ffffff;
    --accent: #c9e6ff;
    --dots: #3f7f95;
  }
  * { box-sizing: border-box; margin: 0; padding: 0; }
  html, body {
    width: 1200px; height: 2418px; overflow: hidden;
    background: var(--page);
    font-family: "Montserrat", Arial, sans-serif;
    color: var(--text);
  }
  .deck { position: relative; width: 1200px; height: 2418px; }
  .slide {
    position: absolute; width: 556px; height: 305px;
    background: radial-gradient(ellipse 60% 65% at 50% 45%, var(--panel-mid) 0%, #13273a 45%, var(--panel-deep) 100%);
    border: 3px solid transparent;
    border-image: linear-gradient(90deg, var(--teal) 0%, #4fd6c8 20%, var(--teal) 45%, var(--blue) 80%, #6fa8e0 100%) 1;
    box-shadow: 0 0 10px rgba(0,169,144,0.55), inset 0 0 10px rgba(49,118,181,0.35);
  }
  .col-left { left: 28px; }
  .col-right { left: 618px; }

  .welcome svg { position: absolute; left: 0; top: 0; }

  .category { text-align: center; }
  .category-kicker { position: absolute; top: 95px; width: 100%; font-size: 35px; font-weight: 600; letter-spacing: 1px; }
  .category-name {
    position: absolute; top: 145px; left: 50%; transform: translateX(-50%);
    border: 2px solid #b8c2ca; padding: 4px 20px 6px; font-size: 39px; font-weight: 600; white-space: nowrap;
    background: rgba(20, 30, 40, 0.4);
  }

  .question-band {
    position: absolute; left: 8px; right: 8px; top: 8px; height: 89px;
    background: var(--band); text-align: center;
  }
  .question-topic { font-size: 31px; font-weight: 600; line-height: 34px; padding-top: 13px; text-shadow: 0 2px 3px rgba(0,0,0,0.6); }
  .question-label { font-size: 31px; font-weight: 600; line-height: 34px; color: var(--accent); letter-spacing: 1px; }
  .question-rule { position: absolute; left: 8px; right: 8px; top: 128px; border-top: 1px dotted var(--dots); }
  .question-number {
    position: absolute; left: 50%; top: 103px; width: 53px; height: 53px; transform: translateX(-50%);
    border: 2px solid #e8eef2; border-radius: 6px; background: #0f1a24;
    font-size: 30px; font-weight: 700; display: flex; align-items: center; justify-content: center;
  }
  .question-text {
    position: absolute; left: 6px; right: 6px; top: 160px; bottom: 8px;
    display: flex; align-items: center; justify-content: center; text-align: center;
    font-size: 25.5px; font-weight: 600; line-height: 28.5px; white-space: nowrap;
  }

  .handoff-text {
    position: absolute; top: 65px; width: 100%; text-align: center;
    font-size: 40px; font-weight: 600; line-height: 47px;
  }
  .handoff-arrow { position: absolute; left: 232px; top: 224px; }

  .answers-title {
    position: absolute; top: 14px; width: 100%; text-align: center;
    font-size: 30px; font-weight: 700; letter-spacing: 1px;
  }
  .answers-underline { position: absolute; left: 190px; width: 176px; top: 55px; height: 5px; background: #e8eef2; border-radius: 3px; }
  .answers-list {
    position: absolute; top: 106px; list-style: none;
    font-size: 18.5px; font-weight: 600; line-height: 32.5px; white-space: nowrap;
  }
  .answers-list.first { left: 38px; }
  .answers-list.second { left: 308px; }
  .answers-list span { display: inline-block; width: 25px; }
</style>
</head>
<body>
<main class="deck">

  <section class="slide welcome col-left" style="top:28px">
    <svg width="550" height="299" viewBox="0 0 550 299" role="img" aria-label="Welcome to Trivia Night!">
      <defs>
        <linearGradient id="neon" x1="0" y1="0" x2="1" y2="1">
          <stop offset="0" stop-color="#ff5ad9"/>
          <stop offset="0.35" stop-color="#ffd94a"/>
          <stop offset="0.7" stop-color="#7dff6a"/>
          <stop offset="1" stop-color="#41e8ff"/>
        </linearGradient>
      </defs>
      <g font-family="Montserrat, Arial, sans-serif" font-weight="700" font-size="51" text-anchor="middle" fill="none" stroke="url(#neon)" stroke-width="2.2">
        <text x="275" y="138">WELCOME TO</text>
        <text x="275" y="198">TRIVIA NIGHT!</text>
      </g>
    </svg>
  </section>

  <section class="slide category col-right" style="top:28px">
    <div class="category-kicker">FIRST CATEGORY</div>
    <div class="category-name">General Knowledge</div>
  </section>

  <section class="slide question col-left" style="top:370px">
    <div class="question-band"><div class="question-topic">General Knowledge</div><div class="question-label">QUESTION</div></div>
    <div class="question-rule"></div><div class="question-number">1</div>
    <p class="question-text">What men’s evening wear got its<br>name from a park in the Hudson<br>Valley where New York’s elite were<br>known to congregate in the 1890s?</p>
  </section>

  <section class="slide question col-right" style="top:370px">
    <div class="question-band"><div class="question-topic">General Knowledge</div><div class="question-label">QUESTION</div></div>
    <div class="question-rule"></div><div class="question-number">2</div>
    <p class="question-text">In the language of international<br>warfare, what do the letters SAM<br>mean?</p>
  </section>

  <section class="slide question col-left" style="top:712px">
    <div class="question-band"><div class="question-topic">General Knowledge</div><div class="question-label">QUESTION</div></div>
    <div class="question-rule"></div><div class="question-number">3</div>
    <p class="question-text">Who is the eldest of the<br>Ashworth sisters?</p>
  </section>

  <section class="slide question col-right" style="top:712px">
    <div class="question-band"><div class="question-topic">General Knowledge</div><div class="question-label">QUESTION</div></div>
    <div class="question-rule"></div><div class="question-number">4</div>
    <p class="question-text">The Louisiana Purchase occurred<br>during the administration of which<br>U.S. President?</p>
  </section>

  <section class="slide question col-left" style="top:1054px">
    <div class="question-band"><div class="question-topic">General Knowledge</div><div class="question-label">QUESTION</div></div>
    <div class="question-rule"></div><div class="question-number">5</div>
    <p class="question-text">Before getting their own long-running<br>series, The Pembertons appeared in<br>animated shorts on a variety show<br>starring what British comedienne?</p>
  </section>

  <section class="slide question col-right" style="top:1054px">
    <div class="question-band"><div class="question-topic">General Knowledge</div><div class="question-label">QUESTION</div></div>
    <div class="question-rule"></div><div class="question-number">6</div>
    <p class="question-text">What was the sub-title of<br>the second Ace Valenti<br>movie?</p>
  </section>

  <section class="slide question col-left" style="top:1396px">
    <div class="question-band"><div class="question-topic">General Knowledge</div><div class="question-label">QUESTION</div></div>
    <div class="question-rule"></div><div class="question-number">7</div>
    <p class="question-text">Who served as Prime Minister of<br>Pakistan from 1988 to 1990 and<br>again from 1993 to 1996?</p>
  </section>

  <section class="slide question col-right" style="top:1396px">
    <div class="question-band"><div class="question-topic">General Knowledge</div><div class="question-label">QUESTION</div></div>
    <div class="question-rule"></div><div class="question-number">8</div>
    <p class="question-text">Which Grand Circuit Baseball team<br>plays its home games at Harbor<br>Yards?</p>
  </section>

  <section class="slide question col-left" style="top:1738px">
    <div class="question-band"><div class="question-topic">General Knowledge</div><div class="question-label">QUESTION</div></div>
    <div class="question-rule"></div><div class="question-number">9</div>
    <p class="question-text">Which planet in our solar system is<br>named for the messenger of the<br>gods in Roman mythology?</p>
  </section>

  <section class="slide question col-right" style="top:1738px">
    <div class="question-band"><div class="question-topic">General Knowledge</div><div class="question-label">QUESTION</div></div>
    <div class="question-rule"></div><div class="question-number">10</div>
    <p class="question-text">Which nation is the only member of<br>ALTRA that does not have a<br>standing army?</p>
  </section>

  <section class="slide handoff col-left" style="top:2080px">
    <p class="handoff-text">Please pass your<br>answers to a<br>neighboring team</p>
    <svg class="handoff-arrow" width="90" height="44" viewBox="0 0 90 44" aria-hidden="true">
      <path d="M3 15 H58 V4 L86 22 L58 40 V29 H3 Z" fill="none" stroke="#e8eef2" stroke-width="3" stroke-linejoin="round"/>
    </svg>
  </section>

  <section class="slide answers col-right" style="top:2080px">
    <h2 class="answers-title">ANSWERS</h2>
    <div class="answers-underline"></div>
    <ol class="answers-list first">
      <li><span>1.</span>Tuxedo</li>
      <li><span>2.</span>Surface to Air Missile</li>
      <li><span>3.</span>Corinne (born in 1979)</li>
      <li><span>4.</span>Thomas Whitfield</li>
      <li><span>5.</span>Tracey Holloway</li>
    </ol>
    <ol class="answers-list second">
      <li>6. When Duty Calls</li>
      <li>7. Farah Rahmani</li>
      <li>8. The Baltimore Larks</li>
      <li>9. Mercury</li>
      <li>10. Iceland</li>
    </ol>
  </section>

</main>
</body>
</html>
```